Change of Address Card

We are fertility physicians in New York . Need a change of address postcard .

The front should be colorful
contain the statement " we are moving!"
and the names Lorenzo Bettuni MD, Oksana Dremova MD

Also the front should contain the drawing of a sperm with either wings or wheeels or whatever your creativity suggests as long as it is not vulgar ( we are doctors !)

The back should contain
the address area and stamp area
and a text area
and possibly a recall of the drawing in front.
use same font

text below

Dear Friends and Colleagues

Lorenzo and Oksana are relocating their fertility practice to a new location on 418 West 71st Street, Suite 604, New York NY 10023
Please take note of our new phone number
Our New phone Number is 212-555-0194

Thank you for your support!

Target Market(s)

this is a card that goes to physicians

Industry/Entity Type

It Support

Requirements
Must have
• fit standard postcard size
Rectangular
At least 3-1/2 inches high x 5 inches long x 0.007 inch thick
No more than 4-1/4 inches high x 6 inches long x 0.016 inches thick
will not be mailed in an envelope

```html
<!DOCTYPE html>
<html lang="en">
<head>
<meta charset="utf-8">
<title>We Are Moving – Postcard</title>
<link href="https://fonts.googleapis.com/css2?family=Poppins:wght@400;600&display=swap" rel="stylesheet">
<style>
  :root {
    --page: #ffffff;
    --card: #ffffff;
    --card-edge: #d6d9de;
    --blue: #6699f5;
    --blue-soft: #c9d8fb;
    --blue-faint: #eef3fe;
    --red: #f0141e;
    --ink: #111111;
    --text: #555a5e;
    --stamp: #9aa3a6;
    --stamp-text: #d4d8da;
    --rule: #8e9799;
  }
  * { box-sizing: border-box; margin: 0; padding: 0; }
  html, body {
    width: 1002px; height: 1200px; overflow: hidden;
    background: var(--page);
    font-family: "Poppins", sans-serif;
  }
  .canvas { position: relative; width: 1002px; height: 1200px; }

  .postcard {
    position: absolute;
    width: 526px; height: 358px;
    background: var(--card);
    border: 1px solid var(--card-edge);
    overflow: hidden;
  }
  .postcard--front { left: 253px; top: 164px; }
  .postcard--back  { left: 264px; top: 720px; }

  /* front */
  .front-disc {
    position: absolute;
    left: -69px; top: 123px;
    width: 292px; height: 292px;
    border-radius: 50%;
    background: var(--blue);
  }
  .artwork {
    position: absolute;
    background: linear-gradient(135deg, var(--blue-faint), var(--blue-soft) 60%, var(--blue-faint));
    border-radius: 40px;
    opacity: .75;
  }
  .artwork--top   { left: 15px;  top: 10px;  width: 340px; height: 130px; }
  .artwork--right { left: 225px; top: 200px; width: 170px; height: 145px; }

  .headline {
    position: absolute; left: 22px; top: 152px;
    font-weight: 600; font-size: 52px; line-height: 60px;
    letter-spacing: -0.5px;
  }
  .headline__we { color: var(--ink); display: block; }
  .headline__are { color: #ffffff; display: block; }
  .headline__moving { color: var(--red); display: block; }
  .headline__moving .o { color: var(--ink); }

  .doctors {
    position: absolute; left: 274px; top: 146px;
    font-weight: 600; font-size: 21px; line-height: 27px;
    color: var(--ink); white-space: pre;
  }

  /* back */
  .back-disc {
    position: absolute;
    left: -95px; top: -71px;
    width: 186px; height: 186px;
    border-radius: 50%;
    background: var(--blue);
  }
  .artwork--back { left: 103px; top: 18px; width: 146px; height: 92px; border-radius: 30px; }

  .stamp-area {
    position: absolute; left: 408px; top: 33px;
    width: 83px; height: 83px;
    border: 2px solid var(--stamp);
    display: flex; align-items: center; justify-content: center;
    text-align: center;
    color: var(--stamp-text);
    font-weight: 600; font-size: 17px; line-height: 24px;
  }
  .address-lines { position: absolute; left: 330px; top: 204px; width: 162px; }
  .address-lines span {
    display: block; height: 22px;
    border-top: 1px solid var(--rule);
  }

  .message {
    position: absolute; left: 30px; top: 136px; width: 270px;
    color: var(--text);
    font-size: 10.6px; line-height: 14.3px;
  }
  .message__greeting { font-weight: 600; font-size: 11.5px; margin-bottom: 14px; }
  .message__signoff { margin-top: 14px; }
</style>
</head>
<body>
<main class="canvas">

  <section class="postcard postcard--front" aria-label="Postcard front">
    <div class="artwork artwork--top" role="img" aria-label="Playful sperm figures whose tails are written as 'we are moving' swimming across the card"></div>
    <div class="artwork artwork--right" role="img" aria-label="More sperm figures with 'we are moving' tails swimming to the right"></div>
    <div class="front-disc"></div>
    <h1 class="headline">
      <span class="headline__we">We</span>
      <span class="headline__are">are</span>
      <span class="headline__moving">m<span class="o">o</span>ving</span>
    </h1>
    <p class="doctors">Lorenzo Bettuni   MD
Oksana Dremova   MD</p>
  </section>

  <section class="postcard postcard--back" aria-label="Postcard back">
    <div class="back-disc"></div>
    <div class="artwork artwork--back" role="img" aria-label="Small sperm figure with a 'we are moving' tail recalling the front"></div>

    <div class="stamp-area">STAMP<br>AREA</div>

    <div class="address-lines" aria-label="Address area">
      <span></span><span></span><span></span><span></span>
    </div>

    <div class="message">
      <p class="message__greeting">Dear Friends and Colleagues,</p>
      <p>Dr. Oksana Dremova and Dr. Lorenzo Bettuni<br>
      are no longer affiliated with Brightpath Fertility<br>
      or Eastline Fertility Services. We are<br>
      excited to announce that we are opening<br>
      a new facility. Our new address, effective<br>
      immediately, is:<br>
      418 West 71st Street, Suite 604<br>
      New York, NY 10023<br>
      Tel: (212) 555-0194</p>
      <p class="message__signoff">Thank you for your support!</p>
    </div>
  </section>

</main>
</body>
</html>
```